email presentation and marketing

we need a email to be used to present our company and services to potential customer. it needs to contain our logo, address, details about our company, photos and a well described text about our work .
I will send a web site from one of the company we are targeting.
The e mail must be sober, elegant, persuasive. The client needs to have the feeling it is dealing to a big company.
See below one of out potential clients
http://qrbdwellings.com/

Target Market(s)

High end custom homes

Industry/Entity Type

Painting And Decorating

Font styles to use
Serif
Sans Serif

Requirements
Must have
• Our name, location, portfolio (need to send some pics), web site http://kz-paintingservices.com.
• Need to develop a email to present our company to potential clients.
Nice to have
• clients reviews.
• we are listed on nest ratings. https://nestratings.com/companies/5816390-kz-custom?service_area=7461025
Should not have
• not colorful

```html
<!DOCTYPE html>
<html lang="en">
<head>
<meta charset="utf-8">
<title>KZ Painting Services</title>
<link rel="stylesheet" href="https://fonts.googleapis.com/css2?family=Roboto:ital,wght@0,400;0,500;0,700;1,400&family=Lato:wght@400;700&display=swap">
<style>
:root{
  --paper:#f1f1f1;
  --slate:#343741;
  --slate-deep:#2a2c33;
  --gold:#e4c713;
  --ink:#1d1d1d;
  --muted:#666;
  --white:#ffffff;
}
*{margin:0;padding:0;box-sizing:border-box}
html,body{width:1200px;height:3093px;overflow:hidden;background:var(--paper)}
body{position:relative;font-family:"Roboto",Arial,sans-serif;color:var(--ink)}
.abs{position:absolute}
.header{left:0;top:0;width:1200px;height:313px;background:var(--paper)}
.brand{display:flex;align-items:center;gap:14px;left:250px;top:130px}
.brand-mark{width:38px;height:38px;background:var(--gold)}
.brand-name{font-family:"Roboto",sans-serif;font-weight:700;font-size:30px;color:var(--gold);line-height:1.1}
.contact{right:254px;top:70px;text-align:right;font-size:20px;line-height:24px}
.contact .phone{font-weight:500;margin-bottom:38px}
.contact .addr{margin-bottom:18px}
.band{left:0;top:313px;width:1200px;height:1147px;background:var(--slate)}
.photo{background:linear-gradient(180deg,#d9dde2 0%,#b9b4ab 45%,#7d756b 70%,#4f5a3d 100%)}
.hero{left:58px;top:357px;width:1080px;height:598px}
.side-l{left:0;top:370px;width:58px;height:535px;background:linear-gradient(90deg,#cfcfcf,#8b8b8b)}
.side-r{left:1138px;top:370px;width:62px;height:535px;background:linear-gradient(90deg,#7e7e7e,#d6d6d6)}
.tagline{left:239px;top:907px;width:722px;height:72px;background:var(--gold);display:flex;align-items:center;justify-content:center;font-weight:700;font-size:26px;color:var(--ink)}
.card{left:239px;top:979px;width:722px;height:444px;background:var(--white);border-radius:0 0 16px 16px}
.about{left:29px;top:48px;width:412px;font-family:"Lato",sans-serif;font-size:19px;line-height:30.5px;color:#222}
.divider{left:478px;top:40px;width:1px;height:235px;background:#e2e2e2}
.services{left:497px;top:48px;list-style:none;font-weight:700;font-size:16px;line-height:22px}
.services li{margin-bottom:30px}
.btn{width:299px;height:43px;border-radius:22px;background:var(--gold);display:flex;align-items:center;justify-content:center;font-weight:500;font-size:22px;color:var(--ink)}
.card .btn{left:211px;top:334px}
.section-title{left:0;width:1200px;text-align:center;font-weight:500;font-size:29px}
.review{width:340px;text-align:center;top:1558px}
.review .avatar{display:block;margin:0 auto 30px}
.review .name{font-style:italic;font-size:19px;color:#555;margin-bottom:28px}
.review .job{font-size:15px;color:#666;margin-bottom:20px}
.review .quote{font-style:italic;font-size:14px;line-height:20px;color:#666}
.work-bar{left:239px;top:2190px;width:722px;height:72px;background:var(--slate);color:var(--white);display:flex;align-items:center;justify-content:center;font-weight:700;font-size:27px}
.thumb{top:2285px;width:138px;height:227px}
.footer{left:0;top:2631px;width:1200px;height:394px;background:var(--slate)}
.footer-brand{left:0;top:60px;width:1200px;display:flex;justify-content:center;align-items:center;gap:12px}
.footer-info{left:0;top:154px;width:1200px;text-align:center;color:var(--white);font-size:20px;line-height:24.7px}
.social{left:455px;top:317px;display:flex;gap:14px}
.social span{width:46px;height:46px;border:2px solid #cfd0d4;border-radius:50%}
.legal{left:0;top:3025px;width:1200px;height:68px;background:var(--slate-deep);color:var(--white);font-size:19px;display:flex;align-items:center;justify-content:center}
</style>
</head>
<body>
<header class="abs header">
  <div class="abs brand"><span class="brand-mark"></span><span class="brand-name">KZ Painting Services</span></div>
  <div class="abs contact">
    <p class="phone">Ph: 416 555 0187</p>
    <p class="addr">A: 48 Larkfield Ave, Unit C2 &nbsp;|&nbsp; M4R 2K7<br>Toronto | Ontario</p>
    <p>info@paintingpropros.com<br>http://paintingpropros.com/</p>
  </div>
</header>

<section class="abs band"></section>
<div class="abs photo side-l" role="img" aria-label="Edge of a neighbouring project photo"></div>
<div class="abs photo side-r" role="img" aria-label="Edge of a neighbouring project photo"></div>
<div class="abs photo hero" role="img" aria-label="Large stone custom home with dark roof and lit entrance at dusk"></div>
<div class="abs tagline">KZ PAINTING – WE ARE ALWAYS READY TO SERVE</div>
<div class="abs card">
  <p class="abs about">K.Z Painting Services is a Toronto based company that provides customised home painting, commercial and industrial painting services to Greater Toronto and metropolitan cities. We use modern equipment and superior brand materials to deliver a high-quality work which makes us nothing less then proud.</p>
  <span class="abs divider"></span>
  <ul class="abs services">
    <li>- WALLPAPER<br>&nbsp;INSTALLATION</li>
    <li>- SPRAY FINISH</li>
    <li>- DRYWALL REPAIRS</li>
    <li>- STAIRCASE FINISH</li>
  </ul>
  <a class="abs btn">GET A QUOTE</a>
</div>

<h2 class="abs section-title" style="top:1490px">CLIENT TESTIMONIALS</h2>
<div class="abs review" style="left:249px">
  <svg class="avatar" width="72" height="72" viewBox="0 0 72 72" aria-hidden="true"><circle cx="36" cy="36" r="35" fill="#111"/><circle cx="36" cy="27" r="11" fill="#fff"/><path d="M16 55c3-10 11-14 20-14s17 4 20 14z" fill="#fff"/></svg>
  <p class="name">ELIO</p>
  <p class="job">Paint Of&nbsp; New Homes and Renovations</p>
  <p class="quote">Marco and his staff are reliable, provide great quality and service. myself and my clients are extremely satisfied with his work.</p>
</div>
<div class="abs review" style="left:609px">
  <svg class="avatar" width="72" height="72" viewBox="0 0 72 72" aria-hidden="true"><circle cx="36" cy="36" r="35" fill="#111"/><circle cx="36" cy="27" r="11" fill="#fff"/><path d="M16 55c3-10 11-14 20-14s17 4 20 14z" fill="#fff"/></svg>
  <p class="name" style="font-style:normal">Brvcnstinc</p>
  <p class="job">Painting Of New Home</p>
  <p class="quote">Contractor was hired to paint New home. Staff was friendly, courteous, helpful, clean, proactive, reliable.</p>
</div>
<div class="abs photo" style="left:254px;top:1837px;width:332px;height:328px;background:linear-gradient(180deg,#e6e4e0,#8d8a86 55%,#2b2b2d)" role="img" aria-label="Bedroom with patterned wallpaper feature wall"></div>
<div class="abs photo" style="left:614px;top:1837px;width:332px;height:328px;background:linear-gradient(180deg,#d8d2c8,#6d6a66 55%,#c9c4bb)" role="img" aria-label="Freshly painted living room with fireplace and tall windows"></div>

<div class="abs work-bar">OUR WORKS</div>
<div class="abs photo thumb" style="left:260px;background:linear-gradient(180deg,#d9d4c8,#eeeeea)" role="img" aria-label="Bathroom with freestanding tub under arched windows"></div>
<div class="abs photo thumb" style="left:441px;background:linear-gradient(180deg,#efefef,#3a3a3a 70%,#d8d8d8)" role="img" aria-label="Curved staircase with dark railing"></div>
<div class="abs photo thumb" style="left:623px;background:linear-gradient(180deg,#e8e4de,#8c7a66 60%,#3b2c22)" role="img" aria-label="Hallway with dark hardwood floor"></div>
<div class="abs photo thumb" style="left:802px;background:linear-gradient(180deg,#f0efec,#a8a39b 55%,#4e4642)" role="img" aria-label="Living room with stone fireplace and built-in shelves"></div>
<a class="abs btn" style="left:450px;top:2557px">GET A QUOTE</a>

<footer class="abs footer">
  <div class="abs footer-brand"><span class="brand-mark"></span><span class="brand-name">KZ Painting Services</span></div>
  <div class="abs footer-info">
    <p>KZ Painting Services</p>
    <p>Contact: Marco Teixeira</p>
    <p>416 555 0187|kzpaintingservice12@mailbox.com</p>
    <p>kz-paintingservices.com</p>
  </div>
  <div class="abs social" aria-label="Social links"><span></span><span></span><span></span><span></span><span></span></div>
</footer>
<div class="abs legal">KZ Painting Services © All rights reserved</div>
</body>
</html>
```